Local Restaurant Needs a One Page Breakfast Menu

I own a restaurant and we are going to be starting a new breakfast service. I want a one page menu that is clean, bright, and tongue in cheek. We will only have a limited menu, so there should be plenty of space to work with. I will not want actual food pictures, but more of a cartoon style representations of food. I'd like a modern cartoon style mixed with our current 1950s theme.

Name of Restaurant: Quillby's
Location: 2943 S. Larkmoor. Marrowfield, KS 48316 - Phone: 620-555-3274 (including location is not a requirement)

Breakfast Hours: 6:30 am - 10:30 am

The two colors selected below are not required, but they are the two colors that are featured inside the dining room of the restaurant.

Industry/Entity Type

Restaurant

Colors
8667ad
acd036

Requirements
Must have
• Menu must only be one page (either standard letter or oversized - either would be ok).

Menu items:

Stuffed Omellete. Stuffing choices: cheese, peppers, jalapenos, onions, tomatoes, salsa, sour cream, green onions, sausage, bacon, ham

Quillby's Blintz (thin, stuffed, pancakes): Stuffing choices: chocolate chips, Z&Qs, Tovin's Nibbles, strawberries, blueberries, raspberries, bananas, sour cream

Homemade Coffee Cake

Cinnamon Rolls

Beverages - Coffee, Soda, Milk

Prices not set (use placeholders).

```html
<!DOCTYPE html>
<html lang="en">
<head>
<meta charset="utf-8">
<title>Quillby's Breakfast Menu</title>
<link href="https://fonts.googleapis.com/css2?family=Federo&family=Poiret+One&display=swap" rel="stylesheet">
<style>
  :root {
    --paper: #f3ede3;
    --band: #8a6a4e;
    --ink: #231f1c;
    --brand-red: #e1202a;
    --rule: #a78e6e;
    --footer-ink: #9a8668;
  }
  html, body {
    margin: 0;
    padding: 0;
    width: 927px;
    height: 1200px;
    overflow: hidden;
    background: var(--paper);
  }
  .menu {
    position: relative;
    width: 927px;
    height: 1200px;
    background: var(--paper);
    color: var(--ink);
    font-family: "Poiret One", sans-serif;
    overflow: hidden;
  }
  .header-band {
    position: absolute;
    top: 0;
    left: 0;
  }
  .brand-name {
    position: absolute;
    top: 36px;
    left: 0;
    width: 927px;
    margin: 0;
    text-align: center;
    font-family: "Federo", sans-serif;
    font-weight: 400;
    font-size: 132px;
    line-height: 170px;
    color: var(--brand-red);
  }
  .hours {
    position: absolute;
    top: 222px;
    left: 0;
    width: 927px;
    text-align: center;
    font-size: 26px;
    font-weight: 400;
    margin: 0;
    color: var(--ink);
    -webkit-text-stroke: 0.4px var(--ink);
  }
  .item {
    position: absolute;
    left: 64px;
    width: 800px;
  }
  .item-name {
    margin: 0;
    font-family: "Federo", sans-serif;
    font-weight: 400;
    font-size: 48px;
    line-height: 50px;
    letter-spacing: -1.5px;
    text-transform: uppercase;
    white-space: nowrap;
    transform: scaleX(0.82);
    transform-origin: left center;
    -webkit-text-stroke: 0.8px var(--ink);
  }
  .item-note {
    font-family: "Poiret One", sans-serif;
    font-size: 27px;
    text-transform: none;
    letter-spacing: 0;
    display: inline-block;
    transform: scaleX(1.2);
    transform-origin: left center;
    -webkit-text-stroke: 0.3px var(--ink);
  }
  .item-desc {
    margin: 8px 0 0;
    font-size: 25px;
    line-height: 38px;
    font-weight: 400;
    word-spacing: 3px;
    letter-spacing: 0.4px;
    -webkit-text-stroke: 0.4px var(--ink);
  }
  .price {
    position: absolute;
    right: 14px;
    top: 6px;
    font-family: "Federo", sans-serif;
    font-size: 30px;
  }
  .price sup {
    font-size: 18px;
    vertical-align: 12px;
  }
  .rule {
    position: absolute;
    left: 72px;
    width: 788px;
    height: 0;
    border-top: 1.5px solid var(--rule);
  }
  .footer {
    position: absolute;
    top: 1145px;
    left: 0;
    width: 927px;
    text-align: center;
    font-size: 24px;
    color: var(--footer-ink);
    margin: 0;
    -webkit-text-stroke: 0.3px var(--footer-ink);
  }
  .footer .dot {
    display: inline-block;
    width: 7px;
    height: 7px;
    border-radius: 50%;
    background: var(--footer-ink);
    vertical-align: middle;
    margin: 0 36px;
  }
</style>
</head>
<body>
<main class="menu">
  <svg class="header-band" width="927" height="330" viewBox="0 0 927 330" aria-hidden="true">
    <polygon points="0,0 927,0 927,255 0,330" fill="var(--band)"/>
  </svg>

  <h1 class="brand-name">Quillby's</h1>
  <p class="hours">Breakfast Served 6:30am - 10:30am</p>

  <section class="item" style="top:364px">
    <h2 class="item-name">Stuffed Omellete</h2>
    <span class="price">$7.<sup>99</sup></span>
    <p class="item-desc">Stuffing choices: cheese, peppers, jalapenos, onions, tomatoes, salsa, sour cream, green onions, sausage, bacon, ham</p>
  </section>
  <div class="rule" style="top:524px"></div>

  <section class="item" style="top:570px">
    <h2 class="item-name">Quillby's Blintz <span class="item-note">(thin, stuffed, pancakes)</span></h2>
    <span class="price">$7.<sup>99</sup></span>
    <p class="item-desc">Stuffing choices: chocolate chips, Z&amp;Qs, Tovin's Nibbles, strawberries, blueberries, raspberries, bananas, sour cream</p>
  </section>
  <div class="rule" style="top:733px"></div>

  <section class="item" style="top:770px">
    <h2 class="item-name">Homemade Coffee Cake</h2>
    <span class="price">$7.<sup>99</sup></span>
  </section>
  <div class="rule" style="top:857px"></div>

  <section class="item" style="top:886px">
    <h2 class="item-name">Cinnamon Rolls</h2>
    <span class="price">$7.<sup>99</sup></span>
  </section>
  <div class="rule" style="top:968px"></div>

  <section class="item" style="top:1016px">
    <h2 class="item-name">Beverages</h2>
    <span class="price">$7.<sup>99</sup></span>
    <p class="item-desc" style="margin-top:0">Coffee, Soda, Milk.</p>
  </section>

  <p class="footer">2943 S. Larkmoor, Marrowfield, KS 48316<span class="dot"></span>Phone: 620-555-3274</p>
</main>
</body>
</html>
```